Web Design for Financial Consulting Company

We need a website design for a financial consulting company "Kelvane Consulting". We build financial models, scenario analysis, handle the budgeting process and provide temporary staffing. I have over 10 years of experience. My Excel expertise and analytical savvy has saved clients over $17 million in profit.

Target Market(s)

Small to medium businesses

Industry/Entity Type

Financial Consulting

Number of Pages Required

4 page

Requirements
Must have
• Professional looking
Nice to have
• A little futuristic looking

```html
<!DOCTYPE html>
<html lang="en">
<head>
<meta charset="utf-8">
<title>Kelvane Consulting</title>
<link href="https://fonts.googleapis.com/css2?family=Rubik:wght@400;500;600&family=Montserrat:wght@400;500;600;700&display=swap" rel="stylesheet">
<style>
:root{
  --stage:#000;
  --navy:#0d3a66;
  --navy-deep:#082a4d;
  --ink:#1f2630;
  --muted:#6b6f76;
  --accent:#1c4f86;
  --paper:#f7f7f9;
  --white:#fff;
  --charcoal:#2c2c2d;
  --cta:#2b2be0;
  --foot:#d9d9dc;
  --foot-bar:#b5b5b9;
}
*{margin:0;padding:0;box-sizing:border-box}
html,body{width:1200px;height:2666px;overflow:hidden;background:var(--stage)}
body{position:relative;font-family:"Montserrat",sans-serif;color:var(--ink)}
.abs{position:absolute}
.head{font-family:"Rubik",sans-serif}
.desktop{position:absolute;left:21px;top:47px;width:1003px;height:2593px;background:var(--white);overflow:hidden}
.mobile{position:absolute;left:1004px;top:47px;width:177px;height:2437px;background:var(--white);overflow:hidden}
.photo{position:absolute}
.hero{left:0;top:0;width:1003px;height:638px;background:linear-gradient(120deg,#0b2f55 0%,#0f4477 45%,#0a3561 100%)}
.nav-link{position:absolute;top:22px;font-size:9px;font-weight:600;color:var(--white)}
.brand{position:absolute;display:flex;align-items:center;gap:6px;color:var(--white);font-family:"Rubik",sans-serif;font-weight:500}
.brand i{display:block;border:2px solid currentColor}
.dot{position:absolute;width:10px;height:10px;border-radius:50%;background:var(--white)}
.btn{position:absolute;display:flex;align-items:center;justify-content:center;gap:8px;font-size:8px;font-weight:600;letter-spacing:1px;text-transform:uppercase}
.btn-light{background:var(--white);color:var(--ink)}
.btn-ghost{border:1px solid var(--white);color:var(--white)}
.btn-line{border:1px solid var(--accent);color:var(--accent)}
.btn-cta{background:var(--cta);color:var(--white)}
.eyebrow{position:absolute;font-size:8.5px;font-weight:700;letter-spacing:1.2px;text-transform:uppercase}
.card-title{position:absolute;font-family:"Rubik",sans-serif;font-size:20px;color:var(--ink)}
.card-text{position:absolute;font-size:9.5px;line-height:19px;color:var(--muted);width:177px}
.stat{position:absolute;width:190px;text-align:center;color:var(--white)}
.stat b{display:block;font-family:"Rubik",sans-serif;font-weight:500;font-size:30px;line-height:36px}
.stat span{font-size:10px}
.foot-h{position:absolute;font-family:"Rubik",sans-serif;font-size:14px;color:var(--ink)}
.foot-t{position:absolute;font-size:8.5px;line-height:15px;color:#8a8c92;height:32px;overflow:hidden}
.m-title{position:absolute;font-family:"Rubik",sans-serif;font-size:11px;color:var(--ink);left:12px}
.m-text{position:absolute;left:12px;width:155px;font-size:5.5px;line-height:10px;color:var(--muted)}
.m-stat{position:absolute;width:88px;text-align:center;color:var(--white)}
.m-stat b{display:block;font-family:"Rubik",sans-serif;font-weight:500;font-size:12px}
.m-stat span{font-size:5.5px}
</style>
</head>
<body>

<!-- Desktop layout -->
<main class="desktop">
  <section>
    <div class="photo hero" role="img" aria-label="Business team reviewing charts at a desk, blue toned"></div>
    <div class="brand" style="left:105px;top:18px;font-size:15px"><i style="width:15px;height:15px"></i>KELVANE</div>
    <span class="nav-link" style="left:229px">Home</span>
    <span class="nav-link" style="left:271px">About</span>
    <span class="nav-link" style="left:315px">Services</span>
    <span class="nav-link" style="left:368px">Contact</span>
    <span class="dot" style="left:672px;top:23px"></span>
    <span class="dot" style="left:699px;top:23px"></span>
    <span class="dot" style="left:726px;top:23px"></span>
    <div class="btn btn-ghost" style="left:765px;top:15px;width:98px;height:27px">Work with me</div>

    <div class="eyebrow" style="left:484px;top:169px;color:var(--white)">Lorem Ipsum</div>
    <h1 class="abs head" style="left:484px;top:212px;font-size:48px;line-height:52px;font-weight:500;color:var(--white)">Helping You Build<br>Inner Resilience.</h1>
    <p class="abs" style="left:484px;top:327px;width:335px;font-size:10px;line-height:19px;font-weight:600;color:var(--white)">Lorem Ipsum is simply dummy text of the printing and typesetting industry. Lorem Ipsum has been the industry's standard dummy text ever since the 1500s, when an unknown printer took a galley of type and scrambled it to make a type specimen book.</p>
    <div class="btn btn-light" style="left:484px;top:447px;width:158px;height:29px">Let's work together →</div>
  </section>

  <section class="abs" style="left:0;top:638px;width:1003px;height:782px;background:var(--paper)">
    <div class="eyebrow" style="left:114px;top:33px;color:var(--accent)">About me</div>
    <h2 class="abs head" style="left:114px;top:74px;width:320px;font-size:29px;line-height:39px;font-weight:400">Lorem Ipsum is simply dummy text of the printing and typesetting industry.</h2>
    <span class="abs" style="left:544px;top:37px;width:31px;height:2px;background:var(--accent)"></span>
    <p class="abs" style="left:544px;top:79px;width:285px;font-size:10px;line-height:19px;color:var(--muted)"><b style="color:var(--ink);font-weight:600">Lorem Ipsum</b> is simply dummy text of the printing and typesetting industry. Lorem Ipsum has been the industry's standard dummy text ever since the 1500s, when an unknown printer took a galley of type and scrambled it to make a type specimen book.</p>
    <div class="btn btn-line" style="left:544px;top:249px;width:103px;height:30px">Read more →</div>

    <span class="abs head" style="left:544px;top:328px;font-size:28px;font-weight:600;color:var(--accent);line-height:20px">”</span>
    <div class="photo" style="left:105px;top:353px;width:379px;height:252px;background:linear-gradient(135deg,#c9d3d6,#8e9aa1 55%,#e4e8ea)" role="img" aria-label="Smiling consultant in a grey suit holding a tablet"></div>
    <p class="abs head" style="left:544px;top:387px;width:320px;font-size:20px;line-height:28px">Lorem Ipsum is simply dummy text of the printing and typesetting industry. Lorem Ipsum has been the industry's standard dummy text ever since the 1500s, when an unknown printer took a galley of type and scrambled it to make a type specimen book.</p>

    <h2 class="abs head" style="left:0;width:1003px;top:788px;text-align:center;font-size:28px;font-weight:400;color:var(--ink)">our services</h2>
  </section>

  <section class="abs" style="left:0;top:1420px;width:1003px;height:441px">
    <div class="photo" style="left:111px;top:82px;width:177px;height:120px;background:linear-gradient(135deg,#b7bcc0,#6b737a)" role="img" aria-label="Team meeting around a laptop"></div>
    <div class="photo" style="left:301px;top:82px;width:177px;height:120px;background:linear-gradient(135deg,#2c6bb0,#7ec2ec 55%,#1a4c8a)" role="img" aria-label="Blue financial chart graphic"></div>
    <div class="photo" style="left:490px;top:82px;width:177px;height:120px;background:linear-gradient(135deg,#d9c9a8,#8f7b5c 60%,#e6ddc9)" role="img" aria-label="Calculator, coins and piggy bank"></div>
    <div class="photo" style="left:679px;top:82px;width:177px;height:120px;background:linear-gradient(135deg,#cfe2f1,#6aa6d4 55%,#eef4f8)" role="img" aria-label="Tablet showing pie charts on reports"></div>
    <div class="card-title" style="left:111px;top:217px">services</div>
    <div class="card-title" style="left:301px;top:217px">services</div>
    <div class="card-title" style="left:490px;top:217px">services</div>
    <div class="card-title" style="left:679px;top:217px">services</div>
    <p class="card-text" style="left:111px;top:253px">Lorem ipsum dolor sit amet, consectetur adipiscing elit. Ut elit tellus pulvinar dapibus leo.</p>
    <p class="card-text" style="left:301px;top:253px">Lorem ipsum dolor sit amet, consectetur adipiscing elit. Ut elit tellus pulvinar dapibus leo.</p>
    <p class="card-text" style="left:490px;top:253px">Lorem ipsum dolor sit amet, consectetur adipiscing elit. Ut elit tellus pulvinar dapibus leo.</p>
    <p class="card-text" style="left:679px;top:253px">Lorem ipsum dolor sit amet, consectetur adipiscing elit. Ut elit tellus pulvinar dapibus leo.</p>
  </section>

  <section class="abs" style="left:0;top:1814px;width:1003px;height:218px;background:var(--charcoal)">
    <svg class="abs" style="left:188px;top:66px" width="26" height="18" viewBox="0 0 26 18" fill="none" stroke="#fff" stroke-width="1.5"><rect x="1" y="1" width="24" height="16"/><line x1="5" y1="6" x2="11" y2="6"/><line x1="5" y1="10" x2="11" y2="10"/><rect x="14" y="5" width="8" height="8"/></svg>
    <div class="stat" style="left:105px;top:95px"><b>352</b><span>Projects Completed</span></div>
    <div class="stat" style="left:294px;top:95px"><b>120+</b><span>Happy Customers</span></div>
    <div class="stat" style="left:484px;top:95px"><b>12</b><span>Awards Received</span></div>
    <div class="stat" style="left:672px;top:95px"><b>15</b><span>Years In Service</span></div>
  </section>

  <section class="abs" style="left:0;top:2032px;width:1003px;height:286px;background:var(--paper)">
    <h2 class="abs head" style="left:0;width:1003px;top:64px;text-align:center;font-size:29px;line-height:34px;font-weight:400">If You Have Any Question,<br>Feel Free to Call 123-456-7890</h2>
    <p class="abs" style="left:0;width:1003px;top:148px;text-align:center;font-size:9.5px;line-height:19px;color:var(--muted)">Ac cum nunc vitae ut turpis praesent nunc odio lorem dictumst<br>vestibulum sem pharetra urna pretium.</p>
    <div class="btn btn-cta" style="left:405px;top:190px;width:158px;height:28px">Let's work together →</div>
  </section>

  <footer class="abs" style="left:0;top:2318px;width:1003px;height:275px;background:var(--foot)">
    <div class="brand" style="left:105px;top:57px;font-size:21px;color:var(--accent)"><i style="width:24px;height:24px"></i>KELVANE</div>
    <p class="foot-t" style="left:105px;top:98px;width:170px">Lorem ipsum is simply lorem ipsum dummy text lorem simply lorem</p>
    <span class="dot" style="left:105px;top:145px;background:var(--ink)"></span>
    <span class="dot" style="left:131px;top:145px;background:var(--ink)"></span>
    <span class="dot" style="left:158px;top:145px;background:var(--ink)"></span>
    <div class="foot-h" style="left:303px;top:66px">Services</div>
    <p class="foot-t" style="left:303px;top:98px;width:120px">Lorem Ipsum is simply<br>Lorem Ipsum is simply<br>Lorem Ipsum is simply</p>
    <div class="foot-h" style="left:500px;top:66px">Quick Links</div>
    <p class="foot-t" style="left:500px;top:98px;width:100px">Home<br>About<br>Services</p>
    <div class="foot-h" style="left:697px;top:66px">Contact Info</div>
    <p class="foot-t" style="left:697px;top:98px;width:170px"><b style="color:var(--ink);font-weight:600">Lorem Ipsum</b> is simply dummy text of the printing and typesetting industry.</p>
    <div class="abs" style="left:0;top:208px;width:1003px;height:67px;background:var(--foot-bar)"></div>
    <p class="abs" style="left:105px;top:239px;font-size:8.5px;color:var(--ink)">© 2023 kelvane consulting</p>
  </footer>
</main>

<!-- Mobile layout -->
<main class="mobile">
  <div class="photo" style="left:0;top:0;width:177px;height:274px;background:linear-gradient(140deg,#0b2f55,#0f4477 55%,#0a3561)" role="img" aria-label="Business team reviewing charts, blue toned"></div>
  <div class="brand" style="left:12px;top:9px;font-size:7px"><i style="width:7px;height:7px;border-width:1px"></i>KELVANE</div>
  <svg class="abs" style="left:157px;top:10px" width="8" height="6" viewBox="0 0 8 6" stroke="#fff"><line x1="0" y1="0.5" x2="8" y2="0.5"/><line x1="0" y1="3" x2="8" y2="3"/><line x1="0" y1="5.5" x2="8" y2="5.5"/></svg>
  <div class="eyebrow" style="left:12px;top:56px;font-size:5px;color:var(--white)">Lorem Ipsum</div>
  <h1 class="abs head" style="left:12px;top:76px;font-size:17px;line-height:20px;font-weight:500;color:var(--white)">Helping You Build<br>Inner Resilience.</h1>
  <p class="abs" style="left:12px;top:128px;width:155px;font-size:5.5px;line-height:12px;font-weight:600;color:var(--white)">Lorem Ipsum is simply dummy text of the printing and typesetting industry. Lorem Ipsum has been the industry's standard dummy text ever since the 1500s, when an unknown printer took a galley of type and scrambled it to make a type specimen book.</p>
  <div class="btn btn-light" style="left:12px;top:217px;width:113px;height:19px;font-size:5px">Let's work together →</div>

  <div class="abs" style="left:0;top:274px;width:177px;height:710px;background:var(--paper)"></div>
  <div class="eyebrow" style="left:12px;top:304px;font-size:5px;color:var(--accent)">About me</div>
  <h2 class="abs head" style="left:12px;top:326px;width:155px;font-size:12px;line-height:16px;font-weight:400">Lorem Ipsum is simply dummy text of the printing and typesetting industry.</h2>
  <span class="abs" style="left:12px;top:404px;width:20px;height:1px;background:var(--accent)"></span>
  <p class="m-text" style="top:420px">Lorem Ipsum is simply dummy text of the printing and typesetting industry. Lorem Ipsum has been the industry's standard dummy text ever since the 1500s, when an unknown printer took a galley of type and scrambled it to make a type specimen book.</p>
  <div class="btn btn-line" style="left:12px;top:502px;width:73px;height:19px;font-size:5px">Read more →</div>
  <div class="photo" style="left:12px;top:551px;width:156px;height:102px;background:linear-gradient(135deg,#c9d3d6,#8e9aa1 55%,#e4e8ea)" role="img" aria-label="Smiling consultant holding a tablet"></div>
  <span class="abs head" style="left:12px;top:664px;font-size:12px;font-weight:600;color:var(--accent)">”</span>
  <p class="abs head" style="left:12px;top:686px;width:155px;font-size:9.5px;line-height:15px;font-weight:500">Lorem Ipsum is simply dummy text of the printing and typesetting industry. Lorem Ipsum has been the industry's standard dummy text ever since the 1500s, when an unknown printer took a galley of type and scrambled it to make a type specimen book.</p>
  <h2 class="abs head" style="left:0;width:177px;top:913px;text-align:center;font-size:11.5px;font-weight:400">our services</h2>

  <div class="photo" style="left:9px;top:967px;width:159px;height:106px;background:linear-gradient(135deg,#b7bcc0,#6b737a)" role="img" aria-label="Team meeting around a laptop"></div>
  <div class="m-title" style="left:9px;top:1086px">services</div>
  <p class="m-text" style="left:9px;top:1106px">Lorem ipsum dolor sit amet, consectetur adipiscing elit. Ut elit tellus pulvinar dapibus leo.</p>
  <div class="photo" style="left:9px;top:1145px;width:159px;height:106px;background:linear-gradient(135deg,#2c6bb0,#7ec2ec 55%,#1a4c8a)" role="img" aria-label="Blue financial chart graphic"></div>
  <div class="m-title" style="left:9px;top:1263px">services</div>
  <p class="m-text" style="left:9px;top:1283px">Lorem ipsum dolor sit amet, consectetur adipiscing elit. Ut elit tellus pulvinar dapibus leo.</p>
  <div class="photo" style="left:9px;top:1321px;width:159px;height:106px;background:linear-gradient(135deg,#d9c9a8,#8f7b5c 60%,#e6ddc9)" role="img" aria-label="Calculator, coins and piggy bank"></div>
  <div class="m-title" style="left:9px;top:1439px">services</div>
  <p class="m-text" style="left:9px;top:1459px">Lorem ipsum dolor sit amet, consectetur adipiscing elit. Ut elit tellus pulvinar dapibus leo.</p>
  <div class="photo" style="left:9px;top:1498px;width:159px;height:106px;background:linear-gradient(135deg,#cfe2f1,#6aa6d4 55%,#eef4f8)" role="img" aria-label="Tablet showing pie charts on reports"></div>
  <div class="m-title" style="left:9px;top:1616px">services</div>
  <p class="m-text" style="left:9px;top:1636px">Lorem ipsum dolor sit amet, consectetur adipiscing elit. Ut elit tellus pulvinar dapibus leo.</p>

  <div class="abs" style="left:0;top:1695px;width:177px;height:180px;background:var(--charcoal)"></div>
  <svg class="abs" style="left:38px;top:1723px" width="14" height="10" viewBox="0 0 26 18" fill="none" stroke="#fff" stroke-width="2"><rect x="1" y="1" width="24" height="16"/><rect x="14" y="5" width="8" height="8"/></svg>
  <div class="m-stat" style="left:0;top:1741px"><b>352</b><span>Projects Completed</span></div>
  <div class="m-stat" style="left:89px;top:1741px"><b>120+</b><span>Happy Customers</span></div>
  <div class="m-stat" style="left:0;top:1811px"><b>12</b><span>Awards Received</span></div>
  <div class="m-stat" style="left:89px;top:1811px"><b>15</b><span>Years In Service</span></div>

  <div class="abs" style="left:0;top:1875px;width:177px;height:184px;background:var(--paper)"></div>
  <h2 class="abs head" style="left:0;width:177px;top:1906px;text-align:center;font-size:11.5px;line-height:13px;font-weight:400">If You Have Any Question,<br>Feel Free to Call 123-<br>456-7890</h2>
  <p class="abs" style="left:15px;width:147px;top:1966px;text-align:center;font-size:5.5px;line-height:11px;color:var(--muted)">Ac cum nunc vitae ut turpis praesent nunc odio lorem dictumst vestibulum sem pharetra urna pretium.</p>
  <div class="btn btn-cta" style="left:33px;top:2016px;width:112px;height:19px;font-size:5px">Let's work together →</div>

  <footer class="abs" style="left:0;top:2059px;width:177px;height:378px;background:var(--foot)">
    <div class="brand" style="left:12px;top:28px;font-size:19px;color:var(--accent)"><i style="width:22px;height:22px"></i>KELVANE</div>
    <p class="abs" style="left:15px;width:147px;top:56px;text-align:center;font-size:5.5px;line-height:10px;color:#8a8c92">Lorem ipsum is simply lorem ipsum dummy text lorem ipsum simply</p>
    <span class="dot" style="left:69px;top:103px;width:7px;height:7px;background:var(--ink)"></span>
    <span class="dot" style="left:85px;top:103px;width:7px;height:7px;background:var(--ink)"></span>
    <span class="dot" style="left:101px;top:103px;width:7px;height:7px;background:var(--ink)"></span>
    <div class="abs head" style="left:0;width:177px;top:118px;text-align:center;font-size:9px">Services</div>
    <p class="abs" style="left:0;width:177px;top:139px;text-align:center;font-size:5.5px;line-height:12px;color:#8a8c92">Lorem Ipsum is simply<br>Lorem Ipsum is simply<br>Lorem Ipsum is simply<br>Lorem Ipsum is simply</p>
    <p class="abs" style="left:0;width:177px;top:197px;text-align:center;font-size:5.5px;line-height:12px;color:#8a8c92">Home<br>About<br>Services<br>Contact</p>
    <div class="abs head" style="left:0;width:177px;top:253px;text-align:center;font-size:9px">Contact Info</div>
    <p class="abs" style="left:15px;width:147px;top:278px;text-align:center;font-size:5.5px;line-height:12px;color:#8a8c92">Lorem Ipsum is simply dummy text of the printing and typesetting industry.</p>
    <div class="abs" style="left:0;top:335px;width:177px;height:43px;background:var(--foot-bar)"></div>
    <p class="abs" style="left:0;width:177px;top:353px;text-align:center;font-size:5px;color:var(--ink)">© 2023 kelvane consulting</p>
  </footer>
</main>

</body>
</html>
```